Bref créative
Tamsel Briar Gifts
making every gift "one of a kind!"
Bright & Fun-filled
Marta Fowler
Owner
no address - online only
fowler@tamselbriargifts.example
www.tamselbriargifts.example
I would like my logo on the front in white background.
I would like my logo in black background.

```html
<!DOCTYPE html>
<html lang="en">
<head>
<meta charset="utf-8">
<title>Tamsel Briar Gifts – Stationery</title>
<link href="https://fonts.googleapis.com/css2?family=Montserrat:wght@400;600&display=swap" rel="stylesheet">
<style>
  :root{
    --stage:#2a2a2c;
    --stage-light:#38383b;
    --paper:#ffffff;
    --ink:#5a5a5a;
    --berry:#b3276f;
    --berry-soft:#f1d6e4;
    --night:#1d1d1f;
    --gold:#b09658;
  }
  *{margin:0;padding:0;box-sizing:border-box}
  html,body{width:1200px;height:281px;overflow:hidden}
  body{
    background:radial-gradient(ellipse at 40% 40%,var(--stage-light),var(--stage));
    font-family:"Montserrat",sans-serif;color:var(--ink);position:relative;
  }
  .piece{position:absolute;box-shadow:0 2px 5px rgba(0,0,0,.55);overflow:hidden}
  .brand{font-weight:600;color:var(--berry);white-space:nowrap;display:flex;align-items:center;gap:3px;line-height:1}
  .brand i{display:inline-block;border-radius:50%;background:var(--berry);flex:none}
  .on-dark .brand{color:var(--paper)}
  .on-dark .brand i{background:var(--paper)}
  .small{font-size:3.4px;line-height:4.6px;white-space:nowrap}

  /* logo showcase */
  .logo-show{position:absolute;left:30px;top:44px;width:128px;text-align:center}
  .logo-show .brand{font-size:11px;justify-content:center}
  .logo-show .brand i{width:8px;height:8px}
  .logo-show .tag{font-size:4.5px;color:#cbb3c1;margin-top:4px;white-space:nowrap}

  /* business cards */
  .card{width:82px;height:40px;background:var(--paper);padding:6px}
  .card .brand{font-size:5.5px}
  .card .brand i{width:4px;height:4px}
  .card .band{position:absolute;left:0;right:0;bottom:0;height:7px;background:var(--berry)}
  .card .small{margin-top:6px}
  .on-dark{background:var(--night)}
  .on-dark .small{color:#b8b8b8}
  .on-berry{background:var(--berry)}
  .on-berry .small{color:#fff;margin-top:2px}

  /* letterheads */
  .letter{width:186px;height:246px;background:var(--paper);padding:10px 12px}
  .letter .brand{font-size:6.5px;margin-top:4px}
  .letter .brand i{width:5px;height:5px}
  .letter .contact{position:absolute;right:12px;top:10px;text-align:right;color:#888;font-size:3.2px;line-height:4.2px}
  .letter .mark{position:absolute;left:38px;top:95px;width:110px;height:55px;border-radius:50%;
    background:radial-gradient(var(--berry-soft),transparent 70%)}
  .letter .foot{position:absolute;left:0;right:0;bottom:0;height:5px;background:var(--berry)}

  /* envelopes */
  .env{width:192px;height:54px;background:var(--paper);padding:7px 9px}
  .env .brand{font-size:5.5px}
  .env .brand i{width:4px;height:4px}
  .env .small{color:#888;margin-top:3px}
  .env .band{position:absolute;left:0;right:0;bottom:0;height:6px;background:var(--berry)}
</style>
</head>
<body>
  <div class="logo-show">
    <div class="brand"><i></i>Tamsel Briar Gifts</div>
    <div class="tag">making every gift "one of a kind!"</div>
  </div>

  <!-- business cards -->
  <div class="piece card" style="left:22px;top:180px">
    <div class="brand"><i></i>Tamsel Briar Gifts</div><div class="band"></div>
  </div>
  <div class="piece card on-dark" style="left:112px;top:180px">
    <div class="brand"><i></i>Tamsel Briar Gifts</div>
    <div class="small">Marta Fowler · Owner</div>
  </div>

  <div class="piece card" style="left:12px;top:226px">
    <div class="brand"><i></i>Tamsel Briar Gifts</div><div class="band"></div>
  </div>
  <div class="piece card on-berry" style="left:100px;top:226px">
    <div class="small"><b>Marta Fowler</b><br>Owner<br>fowler@tamselbriargifts.example<br>www.tamselbriargifts.example</div>
  </div>
  <div class="piece card on-dark" style="left:188px;top:226px">
    <div class="brand"><i></i>Tamsel Briar Gifts</div>
    <div class="small">online only</div>
  </div>

  <!-- letterheads -->
  <div class="piece letter" style="left:288px;top:18px">
    <div class="brand"><i></i>Tamsel Briar Gifts</div>
    <div class="contact">Marta Fowler<br>fowler@tamselbriargifts.example<br>www.tamselbriargifts.example</div>
    <div class="mark" role="img" aria-label="Faint logo decoration"></div>
    <div class="foot"></div>
  </div>
  <div class="piece letter" style="left:492px;top:18px">
    <div class="brand"><i></i>Tamsel Briar Gifts</div>
    <div class="contact">Marta Fowler<br>fowler@tamselbriargifts.example<br>www.tamselbriargifts.example</div>
    <div class="mark" role="img" aria-label="Faint logo decoration"></div>
    <div class="foot"></div>
  </div>

  <!-- #10 envelopes -->
  <div class="piece env" style="left:744px;top:118px">
    <div class="brand"><i></i>Tamsel Briar Gifts</div>
    <div class="small">www.tamselbriargifts.example</div>
    <div class="band"></div>
  </div>
  <div class="piece env" style="left:744px;top:184px">
    <div class="brand"><i></i>Tamsel Briar Gifts</div>
    <div class="small">www.tamselbriargifts.example</div>
    <div class="band"></div>
  </div>

  <!-- envelope group -->
  <svg class="piece" style="left:972px;top:16px" width="204" height="74" viewBox="0 0 204 74">
    <rect width="204" height="74" fill="var(--paper)"/>
    <rect width="204" height="26" fill="var(--gold)"/>
    <path d="M0 26 L102 56 L204 26" fill="none" stroke="#ddd" stroke-width=".8"/>
  </svg>
  <div class="piece env" style="left:972px;top:98px;width:204px;height:62px">
    <div class="brand"><i></i>Tamsel Briar Gifts</div>
    <div class="small">www.tamselbriargifts.example</div>
    <div class="band"></div>
  </div>
  <svg class="piece" style="left:960px;top:170px" width="216" height="70" viewBox="0 0 216 70">
    <rect width="216" height="70" fill="var(--paper)"/>
    <path d="M0 0 L108 40 L216 0" fill="none" stroke="#d8d8d8" stroke-width=".8"/>
    <path d="M0 70 L90 34 M216 70 L126 34" fill="none" stroke="#e6e6e6" stroke-width=".8"/>
    <rect y="64" width="216" height="6" fill="var(--berry)"/>
  </svg>
</body>
</html>
```